this is a new company aimed at the automotive glass industry
what we do is repair cracked windscreens its based in western austraila
I like the old dragracing signwritting logos
I want it to stand out thats why ive gone with the name and title
I dont have a logo but if you can think of one that would be great
but not essential
on the back of the business card i would like Quicker Cheaper Better

Reason: More time needed to decide some great designs Have come through on the eleventh

Target Market(s)

automotive (car yards ,car auctions , trucking companys ect )

Industry/Entity Type

Automotive

Contact Information for Business Card

Pane Stoppers ,
Glass Crack repair specialists ,
Dorian Pelletier ,0437 612 084 ,dpelletier@panestopperswa.com.au

```html
<!DOCTYPE html>
<html lang="en">
<head>
<meta charset="UTF-8">
<title>Pane Stoppers – Business Card</title>
<link rel="stylesheet" href="https://fonts.googleapis.com/css2?family=Michroma&family=Roboto+Condensed:wght@500;700&display=swap">
<style>
  :root {
    --page-bg: #ffffff;
    --card-black: #050607;
    --steel: #a9c2cf;
    --ice: #7cc3d4;
    --white: #f4f6f7;
    --glass-deep: #0a1a20;
    --glass-mid: #1f5f6e;
    --glass-bright: #6fc4d3;
  }
  * { box-sizing: border-box; margin: 0; padding: 0; }
  html, body {
    width: 1200px; height: 900px; overflow: hidden;
    background: var(--page-bg);
  }
  .canvas {
    position: relative; width: 1200px; height: 900px;
    display: flex; justify-content: center; align-items: center; gap: 44px;
  }
  .card {
    position: relative; width: 520px; height: 300px;
    background: var(--card-black); overflow: hidden;
  }

  /* Front */
  .card-front__crack {
    position: absolute; inset: 0;
    background:
      radial-gradient(circle at 76% 58%, rgba(90,80,70,0.55) 0 7%, rgba(40,60,70,0.35) 14%, transparent 42%),
      linear-gradient(180deg, transparent 20%, rgba(20,40,48,0.45) 45%, transparent 62%);
  }
  .brand {
    position: absolute; top: 44px; left: 0; right: 0; text-align: center;
  }
  .brand__name {
    font-family: "Michroma", sans-serif; font-size: 38px; letter-spacing: 3px;
    color: var(--steel); text-transform: uppercase; line-height: 1;
  }
  .brand__tagline {
    margin-top: 12px;
    font-family: "Michroma", sans-serif; font-size: 11.5px; letter-spacing: 4.5px;
    color: var(--white);
  }
  .contact {
    position: absolute; left: 0; width: 330px; top: 176px; text-align: center;
    font-family: "Roboto Condensed", sans-serif;
  }
  .contact__name {
    font-size: 17px; font-weight: 700; color: var(--ice); letter-spacing: 0.5px;
    text-transform: uppercase;
  }
  .contact__phone {
    margin-top: 20px; font-size: 19px; font-weight: 500; color: var(--white); letter-spacing: 2.5px;
  }
  .contact__email {
    margin-top: 2px; font-size: 13.5px; font-weight: 500; color: var(--white);
    letter-spacing: 2.2px; text-transform: uppercase;
  }

  /* Back */
  .card-back { padding: 12px 12px 0; }
  .card-back__photo {
    width: 100%; height: 244px;
    background:
      radial-gradient(ellipse at 35% 40%, var(--glass-bright) 0%, var(--glass-mid) 30%, transparent 60%),
      radial-gradient(ellipse at 78% 35%, rgba(111,196,211,0.75) 0%, transparent 40%),
      radial-gradient(ellipse at 12% 30%, rgba(111,196,211,0.6) 0%, transparent 30%),
      var(--glass-deep);
  }
  .card-back__slogan {
    height: 44px; display: flex; justify-content: space-between; align-items: center;
    padding: 0 8px;
    font-family: "Michroma", sans-serif; font-size: 11px; letter-spacing: 6px; color: var(--white);
  }
</style>
</head>
<body>
  <main class="canvas">
    <section class="card card-front">
      <div class="card-front__crack" role="img" aria-label="Cracked windscreen glass with a stone impact point"></div>
      <header class="brand">
        <h1 class="brand__name">Pane Stoppers</h1>
        <p class="brand__tagline">Glass Crack repair specialist</p>
      </header>
      <div class="contact">
        <p class="contact__name">Dorian Pelletier</p>
        <p class="contact__phone">0437 612 084</p>
        <p class="contact__email">dpelletier@panestopperswa.com.au</p>
      </div>
    </section>

    <section class="card card-back">
      <div class="card-back__photo" role="img" aria-label="Close-up of glowing teal broken glass shards"></div>
      <p class="card-back__slogan"><span>Quicker</span><span>Cheaper</span><span>Better</span></p>
    </section>
  </main>
</body>
</html>
```